Brightleaf Oruma needs a new label design for our Kombucha range- 5 Flavours

We need a label design for our Kombucha range. We are looking for a new look that says quality, vibrant, modern, energetic. The design should draw from our brand identity and the Zanzibar landscape, while communicating internationally. We need a label that describes us and catches the consumer's eye as they scan the supermarket shelves.
Each label should have the same design foundation- with a slight difference in colour to reflect the Kombucha Flavour. Our flavours are: Classic, Ginger/Turmeric, Hibiscus, Cinammon/Clove and Lemongrass.
I have attached in order: our current label (all info on label will remain the same), screenshots from our brand book, some images of labels we love. Our kombucha is packed in glass bottles- it may be nice to play with clear cut outs that bring out the colour of the beverage within the label design.
Check us out on Instagram @brightleaforuma for the vibe

```html
<!DOCTYPE html>
<html lang="en">
<head>
<meta charset="utf-8">
<title>Brightleaf Oruma Kombucha Labels</title>
<link rel="stylesheet" href="https://fonts.googleapis.com/css2?family=Luckiest+Guy&family=Poppins:wght@500;600;700&display=swap">
<style>
  :root {
    --bg: #ececec;
    --paper: #ffffff;
    --brand-blue: #1f4e9c;
    --hibiscus: #c91f2f;
    --hibiscus-deep: #9e1424;
    --classic: #f4b41d;
    --classic-deep: #ee8a1c;
    --classic-ink: #b4500c;
    --lemongrass: #2aa84c;
    --lemongrass-deep: #17803a;
    --cinnamon: #e7bb70;
    --cinnamon-deep: #c98f44;
    --cinnamon-ink: #8a5522;
    --ginger: #1f6271;
    --ginger-deep: #164a57;
    --ginger-text: #e6e43a;
  }
  * { box-sizing: border-box; margin: 0; padding: 0; }
  html, body { width: 1200px; height: 900px; overflow: hidden; }
  body {
    background: radial-gradient(circle at 50% 40%, #f6f6f6, var(--bg));
    font-family: "Poppins", sans-serif;
  }
  .label-range {
    position: absolute;
    left: 24px; top: 270px;
    display: flex;
    gap: 18px;
  }
  .label {
    width: 216px; height: 350px;
    background: var(--paper);
    position: relative;
    box-shadow: 0 6px 18px rgba(0,0,0,0.12);
    overflow: hidden;
  }
  .brand {
    height: 150px;
    display: flex;
    flex-direction: column;
    align-items: center;
    justify-content: center;
    gap: 10px;
    padding: 6px 14px 0;
  }
  .brand-name {
    display: flex;
    align-items: center;
    gap: 6px;
    color: var(--brand-blue);
    font-family: "Poppins", sans-serif;
    font-weight: 700;
    font-size: 15px;
    letter-spacing: 0.3px;
    text-transform: uppercase;
    white-space: nowrap;
  }
  .brand-dot {
    flex: none;
    width: 9px; height: 9px;
    border-radius: 50%;
    background: var(--brand-blue);
  }
  .tagline {
    background: var(--brand-blue);
    color: var(--paper);
    font-size: 6px;
    font-weight: 500;
    letter-spacing: 1px;
    padding: 2px 10px;
    border-radius: 2px;
    text-transform: uppercase;
    white-space: nowrap;
  }
  .flavour-band {
    position: absolute;
    left: 0; right: 0; top: 150px; bottom: 0;
    clip-path: polygon(0 0, 40% 0, 50% 9%, 60% 0, 100% 0, 100% 100%, 0 100%);
    display: flex;
    flex-direction: column;
    align-items: center;
    padding-top: 26px;
    background: linear-gradient(160deg, var(--c1), var(--c2));
  }
  .product-name {
    font-family: "Luckiest Guy", sans-serif;
    font-weight: 400;
    font-size: 26px;
    line-height: 1.1;
    text-transform: uppercase;
    white-space: nowrap;
    color: var(--name-ink);
    text-shadow: 2px 2px 0 var(--paper), -1px -1px 0 var(--paper), 1px -1px 0 var(--paper), -1px 1px 0 var(--paper);
  }
  .flavour-art {
    width: 72px; height: 48px;
    margin-top: 10px;
    border-radius: 8px;
    background: var(--art);
  }
  .flavour-name {
    margin-top: 12px;
    padding: 2px 8px;
    font-size: 10px;
    font-weight: 600;
    letter-spacing: 1px;
    text-transform: uppercase;
    white-space: nowrap;
    border-radius: 2px;
    background: var(--pill-bg);
    color: var(--pill-ink);
  }
  .volume {
    margin-top: 10px;
    padding: 1px 10px;
    font-size: 9px;
    font-weight: 600;
    border: 2px solid var(--vol-ink);
    border-radius: 10px;
    color: var(--vol-ink);
  }
  .hibiscus { --c1: var(--hibiscus); --c2: var(--hibiscus-deep); --name-ink: var(--hibiscus); --art: rgba(255,255,255,0.35); --pill-bg: var(--paper); --pill-ink: var(--hibiscus); --vol-ink: var(--paper); }
  .classic { --c1: var(--classic); --c2: var(--classic-deep); --name-ink: var(--classic-deep); --art: rgba(255,255,255,0.25); --pill-bg: var(--classic-deep); --pill-ink: var(--paper); --vol-ink: var(--classic-ink); }
  .lemongrass { --c1: var(--lemongrass); --c2: var(--lemongrass-deep); --name-ink: var(--lemongrass); --art: rgba(255,255,255,0.35); --pill-bg: var(--paper); --pill-ink: var(--lemongrass-deep); --vol-ink: var(--paper); }
  .cinnamon { --c1: var(--cinnamon); --c2: var(--cinnamon-deep); --name-ink: var(--cinnamon-deep); --art: rgba(120,70,30,0.3); --pill-bg: var(--cinnamon-deep); --pill-ink: var(--paper); --vol-ink: var(--cinnamon-ink); }
  .ginger { --c1: var(--ginger); --c2: var(--ginger-deep); --name-ink: var(--ginger); --art: rgba(230,228,58,0.4); --pill-bg: var(--ginger-deep); --pill-ink: var(--ginger-text); --vol-ink: var(--ginger-text); }
</style>
</head>
<body>
  <main class="label-range">
    <section class="label hibiscus">
      <header class="brand">
        <div class="brand-name"><span class="brand-dot"></span>Brightleaf Oruma</div>
        <div class="tagline">Heal your body • Heal your mind</div>
      </header>
      <div class="flavour-band" role="img" aria-label="Red band with palm tree silhouettes">
        <h2 class="product-name">Kombucha</h2>
        <div class="flavour-art" role="img" aria-label="Line drawing of a hibiscus flower"></div>
        <p class="flavour-name">Hibiscus</p>
        <p class="volume">350 ML</p>
      </div>
    </section>
    <section class="label classic">
      <header class="brand">
        <div class="brand-name"><span class="brand-dot"></span>Brightleaf Oruma</div>
        <div class="tagline">Heal your body • Heal your mind</div>
      </header>
      <div class="flavour-band" role="img" aria-label="Yellow band with palm tree silhouettes">
        <h2 class="product-name">Kombucha</h2>
        <div class="flavour-art" role="img" aria-label="Soft palm leaf texture"></div>
        <p class="flavour-name">Classic</p>
        <p class="volume">350 ML</p>
      </div>
    </section>
    <section class="label lemongrass">
      <header class="brand">
        <div class="brand-name"><span class="brand-dot"></span>Brightleaf Oruma</div>
        <div class="tagline">Heal your body • Heal your mind</div>
      </header>
      <div class="flavour-band" role="img" aria-label="Green band with palm tree silhouettes">
        <h2 class="product-name">Kombucha</h2>
        <div class="flavour-art" role="img" aria-label="Line drawing of lemongrass stalks"></div>
        <p class="flavour-name">Lemongrass</p>
        <p class="volume">350 ML</p>
      </div>
    </section>
    <section class="label cinnamon">
      <header class="brand">
        <div class="brand-name"><span class="brand-dot"></span>Brightleaf Oruma</div>
        <div class="tagline">Heal your body • Heal your mind</div>
      </header>
      <div class="flavour-band" role="img" aria-label="Tan band with palm tree silhouettes">
        <h2 class="product-name">Kombucha</h2>
        <div class="flavour-art" role="img" aria-label="Line drawing of a cinnamon stick"></div>
        <p class="flavour-name">Cinammon | Clove</p>
        <p class="volume">350 ML</p>
      </div>
    </section>
    <section class="label ginger">
      <header class="brand">
        <div class="brand-name"><span class="brand-dot"></span>Brightleaf Oruma</div>
        <div class="tagline">Heal your body • Heal your mind</div>
      </header>
      <div class="flavour-band" role="img" aria-label="Teal band with palm tree silhouettes">
        <h2 class="product-name">Kombucha</h2>
        <div class="flavour-art" role="img" aria-label="Line drawing of ginger and turmeric roots"></div>
        <p class="flavour-name">Ginger | Turmeric</p>
        <p class="volume">350 ML</p>
      </div>
    </section>
  </main>
</body>
</html>
```